Computer consultant website

Vexlo Software is a newly started computer consulting company. It's a small one-man company that provides mostly Android applications but also websites in collaboration with designers. I'm running this company on the side of full time university studies.

I'm in need of a website which will function as:
Primarily - I'll direct potential clients to the page so they can read about the company, what i offer and past work.
Secondarily - Making my company visible through the web and maybe getting new clients.

The final design should look modern, clean and professional.

Pages that will be in the final website are (Note that it's not the exact titles as the page will not be in english):
* About
* Services (what Vexlo offers)
* Portfolio/work
* Short news (like PlanHives "News and press")
* Contact.

Inspiration
http://www.planhive.example/design/87836
http://www.brambleorb.example/
http://www.planhive.example/design/845881
http://www.planhive.example/design/1369424 - Lighter design, however a bit cluttered.

No programming code is needed delivered at all. Focus on designing rather then coding.

If you have any questions, do not hesitate to send me a message.

Target Market(s)

Non-technical entrepreneurs and small companies.

Industry/Entity Type

University

Requirements
Must have
• Must have my company logo (see attachment).

Must in any way use both colors from my logo.

A way to logically rearrange content to fit smaller screens. I will implement this design so that it can be pleasantly viewed on mobile devices. You don't necessarily need to provide exactly how the design would look on mobile devices.

I need the following types of page designs:
* Landing page
* Content page
* Portfolio/work (with accompanying inside/clicked) page

Landing/start page must in any way include at least the information:
* Shorter version of "About Vexlo"
* At least 1 most recent portfolio/work entry
* At least 1 most recent news entry
* Services that Vexlo offers.
Nice to have
Should not have
• Testimonials or newsletter.

```html
<!DOCTYPE html>
<html lang="en">
<head>
<meta charset="utf-8">
<title>Vexlo Software</title>
<link href="https://fonts.googleapis.com/css2?family=Source+Sans+3:wght@400;600;700&display=swap" rel="stylesheet">
<style>
:root{
  --canvas:#f0f0f0;
  --white:#ffffff;
  --blue:#2176f5;
  --blue-dark:#1558c8;
  --ink:#222222;
  --body:#555555;
  --muted:#777777;
  --dark:#343132;
  --footer:#1b1b1b;
  --line:#dddddd;
}
*{box-sizing:border-box;margin:0;padding:0}
html,body{width:1200px;height:900px;overflow:hidden}
body{background:var(--canvas);font-family:"Source Sans 3",Arial,sans-serif;color:var(--ink);position:relative}
.page{position:absolute;left:200px;top:9px;width:801px;height:883px;background:var(--white)}
.abs{position:absolute}

/* header */
.site-header{left:0;top:0;width:801px;height:68px;background:linear-gradient(#ffffff,#e9e9e9);border-bottom:1px solid #dcdcdc}
.brand{left:99px;top:16px;display:flex;align-items:center;gap:10px}
.brand-mark{width:36px;height:36px;border-radius:50%;background:var(--blue)}
.brand-name{font-size:31px;font-weight:600;color:var(--ink);line-height:1}
.main-nav{left:327px;top:0;display:flex;height:68px}
.main-nav a{display:block;height:68px;line-height:70px;padding:0 10px;font-size:12.5px;color:#333;text-decoration:none;border-right:1px solid #dedede}
.main-nav a:first-child{border-left:1px solid #dedede}
.main-nav a.active{background:linear-gradient(#3f8cff,var(--blue));color:#fff;position:relative}
.main-nav a.active::after{content:"";position:absolute;left:50%;bottom:-6px;margin-left:-6px;border:6px solid transparent;border-bottom:0;border-top-color:var(--blue)}

/* hero */
.hero{left:0;top:68px;width:801px;height:206px;overflow:hidden}
.hero-title{left:106px;top:71px;font-size:31px;font-weight:400;color:var(--ink);line-height:1}
.hero-title span{color:var(--blue)}
.hero-text{left:106px;top:104px;width:260px;font-size:14px;line-height:17px;color:#333}
.btn{display:inline-block;background:linear-gradient(#4a93ff,var(--blue));color:#fff;border:1px solid var(--blue-dark);border-radius:10px;font-size:11px;text-decoration:none;padding:3px 9px;box-shadow:0 2px 2px rgba(0,0,0,.2)}
.hero-btn{right:447px;top:151px;font-size:11.5px;padding:3px 9px}
.hero-photo{left:358px;top:11px;width:359px;height:195px;background:linear-gradient(90deg,#c9d3e0,#8a96a8 55%,#3c3f48)}
.arrow{width:26px;height:26px}
.arrow-prev{left:33px;top:86px}
.arrow-next{left:741px;top:86px}

/* feature band */
.features{left:0;top:274px;width:801px;height:72px;background:var(--blue);display:flex;padding-left:88px}
.feature{width:225px;padding:8px 0 0 0;display:flex;gap:9px;border-right:1px solid rgba(0,0,0,.12)}
.feature:last-child{border-right:0}
.feature svg{flex:none}
.feature h3{font-size:15px;font-weight:400;color:#fff;line-height:18px;margin-top:1px}
.feature p{font-size:9px;font-weight:600;color:#fff;line-height:11.5px;margin-top:4px;width:145px}

/* intro */
.welcome{left:94px;top:385px;width:392px}
.welcome h2{font-size:20px;font-weight:400;color:var(--ink)}
.welcome h2 span{color:var(--blue);font-weight:600}
.welcome .lead{font-size:8px;font-weight:600;line-height:12px;margin-top:5px;color:#111}
.welcome .copy{font-size:7.8px;line-height:11.8px;color:var(--body);margin-top:11px}
.welcome .btn{margin-top:13px;font-size:9.5px;padding:2px 8px}

.services{left:540px;top:386px;width:180px}
.services h2{font-size:19px;font-weight:400;color:var(--blue)}
.services .lead{font-size:8px;font-weight:600;line-height:11px;margin-top:5px;color:#111}
.services ul{list-style:none;margin-top:6px}
.services li{font-size:8px;color:var(--body);line-height:14.5px;padding-left:8px;position:relative}
.services li::before{content:"";position:absolute;left:0;top:5px;width:4px;height:4px;border-radius:50%;background:var(--blue)}
.news-item{margin-top:10px;padding-top:7px;border-top:1px solid var(--line)}
.news-item h3{font-size:12px;font-weight:400;color:var(--blue);line-height:14px}
.news-item p{font-size:8px;color:var(--body);line-height:11px;margin-top:2px}
.news-item time{color:var(--muted);font-weight:600}

/* portfolio */
.portfolio{left:0;top:622px;width:801px;height:224px;background:var(--dark);border-top:3px solid var(--blue)}
.portfolio-tab{left:345px;top:600px;width:115px;height:22px;background:var(--blue);color:#fff;font-size:14px;text-align:center;line-height:22px;clip-path:polygon(4% 0,96% 0,100% 100%,0 100%)}
.cards{left:101px;top:27px;display:flex;gap:31px}
.card{width:179px;height:167px;background:linear-gradient(#fff 80%,#e4e4e4);padding:4px;box-shadow:0 5px 6px rgba(0,0,0,.5);text-align:center}
.card-photo{height:98px;background:linear-gradient(135deg,#b8c4d2,#5f6c80)}
.card h3{font-size:15px;font-weight:400;color:var(--blue);margin-top:5px;padding-bottom:2px;border-bottom:1px solid var(--line)}
.card p{font-size:9.5px;color:#333;line-height:11px;margin-top:5px}

/* footer */
.site-footer{left:0;top:846px;width:801px;height:37px;background:var(--footer);font-size:8.5px;color:#666}
.copyright{left:103px;top:13px}
.footer-nav{left:443px;top:13px;display:flex;gap:16px}
.footer-nav a{color:#666;text-decoration:none}
.footer-nav a.active{color:#fff}
</style>
</head>
<body>
<div class="page">
  <header class="site-header abs">
    <div class="brand abs"><span class="brand-mark"></span><span class="brand-name">Vexlo</span></div>
    <nav class="main-nav abs">
      <a class="active" href="#">Home</a><a href="#">About Us</a><a href="#">Services</a><a href="#">Portfolio</a><a href="#">News</a><a href="#">Contact Us</a>
    </nav>
  </header>

  <section class="hero abs">
    <div class="hero-photo abs" role="img" aria-label="Business team in suits working around a laptop in an office"></div>
    <h1 class="hero-title abs">Lorem <span>ipsum dolor</span></h1>
    <p class="hero-text abs">Sit amet, consectetur adipiscing elit. Nulla lobortis consequat mauris, eget eleifend</p>
    <a class="btn hero-btn abs" href="#">Read more</a>
    <svg class="arrow arrow-prev abs" viewBox="0 0 26 26"><circle cx="13" cy="13" r="12" fill="#333" stroke="#2176f5" stroke-width="2"/><path d="M15 8l-5 5 5 5" fill="none" stroke="#fff" stroke-width="2.4"/></svg>
    <svg class="arrow arrow-next abs" viewBox="0 0 26 26"><circle cx="13" cy="13" r="12" fill="#333" stroke="#2176f5" stroke-width="2"/><path d="M11 8l5 5-5 5" fill="none" stroke="#fff" stroke-width="2.4"/></svg>
  </section>

  <section class="features abs">
    <div class="feature">
      <svg width="26" height="26" viewBox="0 0 26 26"><circle cx="12" cy="12" r="10" fill="none" stroke="#111" stroke-width="2"/><ellipse cx="12" cy="12" rx="4" ry="10" fill="none" stroke="#111" stroke-width="1.6"/><path d="M2 12h20M4 7h16M4 17h16" stroke="#111" stroke-width="1.4"/><path d="M15 14l8 4-3 1 2 4-2 1-2-4-3 2z" fill="#111" stroke="#fff" stroke-width=".8"/></svg>
      <div><h3>Lorem ipsum dolor sit</h3><p>Consectetur adipiscing elit. Nulla lobortis consequat mauris, eget eleifend nunc viverra viverra.</p></div>
    </div>
    <div class="feature">
      <svg width="26" height="26" viewBox="0 0 26 26"><path d="M13 2a7 7 0 0 0-4 12.7V18h8v-3.3A7 7 0 0 0 13 2z" fill="none" stroke="#111" stroke-width="2"/><path d="M9 20h8M10 23h6" stroke="#111" stroke-width="2"/></svg>
      <div><h3>Lorem ipsum dolor sit</h3><p>Consectetur adipiscing elit. Nulla lobortis consequat mauris, eget eleifend nunc viverra viverra.</p></div>
    </div>
    <div class="feature">
      <svg width="26" height="26" viewBox="0 0 26 26"><path d="M3 2h11l6 6v8M3 2v22h12" fill="none" stroke="#111" stroke-width="2.4"/><path d="M14 2v6h6" fill="none" stroke="#111" stroke-width="2"/><path d="M20 16v9M15.5 20.5h9" stroke="#111" stroke-width="2.6"/></svg>
      <div><h3>Lorem ipsum dolor sit</h3><p>Consectetur adipiscing elit. Nulla lobortis consequat mauris, eget eleifend nunc viverra viverra.</p></div>
    </div>
  </section>

  <section class="welcome abs">
    <h2>Welcome to <span>Vexlo</span></h2>
    <p class="lead">Lorem ipsum dolor sit amet, consectetur adipiscing elit. Nulla lobortis consequat mauris, eget eleifend nunc viverra viverra. Ut ac risus odio. Aliquam pretium purus sed nulla feugiat blandit.</p>
    <p class="copy">Cras vel libero ut lacus eleifend tempor. Phasellus eleifend, magna non tincidunt accumsan, justo arcu cursus ipsum, non porttitor sapien quam vel magna. Maecenas elit nisl, molestie nec dapibus nec, aliquet a erat. Donec scelerisque lacus a libero suscipit auctor volutpat enim euismod. Mauris porta, lacus ut ullamcorper sodales, mauris tortor feugiat purus, nec aliquam neque purus ac metus. Nunc eleifend leo quis nisl hendrerit ultrices. Suspendisse quis feugiat elit. Fusce vitae dolor ac est tincidunt feugiat. Phasellus volutpat dui in sapien malesuada tempus placerat justo ultricies. Duis mollis ornare risus, ut consectetur mi tincidunt sit amet. Maecenas quis nibh ac orci tempus scelerisque ac et massa Maecenas quis nibh ac orci tempus scelerisque ac et massa.</p>
    <a class="btn" href="#">Read more</a>
  </section>

  <section class="services abs">
    <h2>Our Services</h2>
    <p class="lead">Lorem ipsum dolor sit amet, consectetur adipiscing elit. Nulla lobortis consequat mauris,</p>
    <ul>
      <li>Cras vel libero ut lacus eleifend tempor.</li>
      <li>Phasellus eleifend, magna non tincidunt</li>
      <li>Accumsan, justo arcu cursus ipsum, non</li>
      <li>Porttitor sapien quam vel magna. Maecenas</li>
      <li>Elit nisl, molestie nec dapibus nec, aliquet a</li>
      <li>Erat. Donec scelerisque lacus a libero suscipit</li>
      <li>Auctor volutpat enim euismod. Mauris porta,</li>
    </ul>
    <article class="news-item">
      <h3>Latest News</h3>
      <p><time>12.03</time> &ndash; Lorem ipsum dolor sit amet, consectetur elit.</p>
    </article>
  </section>

  <div class="portfolio-tab abs">Portfolio</div>
  <section class="portfolio abs">
    <div class="cards abs">
      <article class="card"><div class="card-photo" role="img" aria-label="Team meeting around a white table seen from above"></div><h3>Lorem ipsum dolor sit</h3><p>Consectetur adipiscing elit. Nulla lobortis consequat mauris, eget</p></article>
      <article class="card"><div class="card-photo" role="img" aria-label="Business people discussing at a meeting table"></div><h3>Lorem ipsum dolor sit</h3><p>Consectetur adipiscing elit. Nulla lobortis consequat mauris, eget</p></article>
      <article class="card"><div class="card-photo" role="img" aria-label="Office team gathered around a desk in a bright room"></div><h3>Lorem ipsum dolor sit</h3><p>Consectetur adipiscing elit. Nulla lobortis consequat mauris, eget</p></article>
    </div>
  </section>

  <footer class="site-footer abs">
    <p class="copyright abs">Copyright information comes here</p>
    <nav class="footer-nav abs"><a class="active" href="#">Home</a><a href="#">About Us</a><a href="#">Services</a><a href="#">Portfolio</a><a href="#">News</a><a href="#">Contact Us</a></nav>
  </footer>
</div>
</body>
</html>
```